RDW Drifting Marigold, American Quarter Horse Stallion Stud Services

Advertisement for stud service. I'd like to showcase how stunningly beautiful this horse is with the full-body pic and how sweet, gentle, and quiet he is with the other pic. I want two-sided cards with photos on both sides. Headshot (cropped) on front with info on management, contact #s, etc. Full-body, pairup.example-type pic on back with some information on his pedigree. I'd like something striking enough that even if people don't want the service, they keep the card.

Target Market(s)

Horse owners, horse breeders, horse trainers, equestrians

Contact Information for Business Card

Horse's name: RDW Drifting Marigold
Owner: Noreen Castell
Manager: Trudy Wexmoor
Phone: 208-555-0148
Pedigree information: Sire - Oaks Bonne Lucette, Dam - Quiet Dancing Lorabel
Sire's parents: Brightwater Tam 41 (sire) and Cedar Gentle Lass (dam)
Dam's parents: Shez Dorabel (sire) and Bold Hearted Rhyme (dam)

Font styles to use
Sans Serif

Requirements
Must have
• Rich, distinctive look. Should be a stand-out card; one that people keep even if they're not interested in the service.
Nice to have
• Pedigree information displayed in a family-tree arrangement. The horse is black, so I am picturing cards that are mostly black, probably with white or off-white (cream-colored) lettering. In fact, the horse has what's known as the cream-color gene, so maybe cream-colored would be better.

```html
<!DOCTYPE html>
<html lang="en">
<head>
<meta charset="utf-8">
<title>RDW Drifting Marigold – Stud Service Cards</title>
<link href="https://fonts.googleapis.com/css2?family=Roboto+Condensed:wght@300;400&display=swap" rel="stylesheet">
<style>
  :root {
    --backdrop: #e4e4e7;
    --card-dark: #1d1925;
    --card-sheen: #3a3344;
    --rule: #f4f3f6;
    --ink: #ecebf0;
    --photo-sand: #8a7a66;
    --photo-dark: #1a1616;
    --photo-grass: #6f8a4a;
  }
  * { margin: 0; padding: 0; box-sizing: border-box; }
  html, body {
    width: 1200px; height: 798px; overflow: hidden;
    background: var(--backdrop);
    font-family: "Roboto Condensed", "Arial Narrow", sans-serif;
    color: var(--ink);
  }
  .sheet { position: relative; width: 1200px; height: 798px; }
  .card {
    position: absolute; top: 236px;
    width: 570px; height: 326px;
    background: linear-gradient(115deg, var(--card-dark) 0%, var(--card-sheen) 45%, var(--card-dark) 70%, var(--card-dark) 100%);
    overflow: hidden;
    box-shadow: 0 6px 18px rgba(0,0,0,.18);
  }
  .card--front { left: 20px; }
  .card--back { left: 610px; }
  .card svg { position: absolute; inset: 0; }

  /* front */
  .contact {
    position: absolute; left: 26px; top: 22px;
    font-weight: 300; font-size: 17px; line-height: 1.25;
  }
  .contact dt { margin-top: 10px; }
  .contact dt:first-child { margin-top: 0; }
  .contact dd { padding-left: 12px; }
  .front-name {
    position: absolute; left: 18px; top: 244px;
    font-size: 29px; font-weight: 400; letter-spacing: .2px;
  }

  /* back */
  .pedigree {
    position: absolute; left: 0; top: 24px; width: 190px;
    text-align: center; font-weight: 300; font-size: 15.5px; line-height: 1.3;
  }
  .pedigree h2 { font-weight: 300; font-size: 16px; margin-bottom: 16px; }
  .pedigree .gen { margin-bottom: 16px; }
  .back-name {
    position: absolute; left: 196px; right: 0; top: 256px; height: 70px;
    display: flex; align-items: center; justify-content: center;
    font-size: 31px; font-weight: 400;
  }
</style>
</head>
<body>
<main class="sheet">

  <section class="card card--front" aria-label="Card front">
    <svg width="570" height="326" viewBox="0 0 570 326">
      <defs>
        <linearGradient id="headshot" x1="0" y1="0" x2="1" y2="1">
          <stop offset="0" stop-color="var(--photo-sand)"/>
          <stop offset=".55" stop-color="var(--photo-dark)"/>
          <stop offset="1" stop-color="#3b2c24"/>
        </linearGradient>
      </defs>
      <polygon points="238,0 570,0 570,326 346,326" fill="var(--rule)"/>
      <polygon points="246,0 570,0 570,326 354,326" fill="url(#headshot)" role="img" aria-label="Cropped headshot photo of the black stallion under saddle"/>
      <polygon points="0,212 283,212 285,218 0,218" fill="var(--rule)"/>
    </svg>
    <dl class="contact">
      <dt>Owner</dt><dd>Noreen Castell</dd>
      <dt>Manager</dt><dd>Trudy Wexmoor</dd>
      <dt>Phone</dt><dd>208-555-0148</dd>
    </dl>
    <div class="front-name">RDW Drifting Marigold</div>
  </section>

  <section class="card card--back" aria-label="Card back">
    <svg width="570" height="326" viewBox="0 0 570 326">
      <defs>
        <linearGradient id="fullbody" x1="0" y1="0" x2="0" y2="1">
          <stop offset="0" stop-color="#6e7a5a"/>
          <stop offset=".5" stop-color="var(--photo-dark)"/>
          <stop offset="1" stop-color="var(--photo-grass)"/>
        </linearGradient>
      </defs>
      <rect x="190" y="0" width="6" height="326" fill="var(--rule)"/>
      <rect x="196" y="0" width="374" height="256" fill="var(--rule)"/>
      <rect x="202" y="6" width="368" height="244" fill="url(#fullbody)" role="img" aria-label="Full-body conformation photo of the black stallion standing on a lawn"/>
    </svg>
    <div class="pedigree">
      <h2>Pedigree information:</h2>
      <p class="gen">Sire: Oaks Bonne Lucette<br>Dam: Quiet Dancing Lorabel</p>
      <p class="gen">Sire's parents:<br>Sire: Brightwater Tam 41<br>Dam: Cedar Gentle Lass</p>
      <p class="gen">Dam's parents:<br>Sire: Shez Dorabel<br>Dam: Bold Hearted Rhyme</p>
    </div>
    <div class="back-name">RDW Drifting Marigold</div>
  </section>

</main>
</body>
</html>
```